Homes, Invest in Non-performing loans

We need only 3 web pages, one for the home, one for the content, one for the properties.
The main focus of our business is to offer non performing loans (before foreclosures) to the general public. All the non-performing mortgages will end in a house, an apartment, a store, etc.
Our customers are able to invest from 10,000usd to 1,000,000usd (average 50,000usd).
Our customers' usual focus groups are employees who want second earnings, perceiving the business feeling without outlay time. They look for a solid finance sense corporation that confers them certainty.
Nearly all our clients desire the house, apartment, store, etc. more than the actual earnings.
The name of our company is BRAMLEY
Reason: We value the time and effort you already invest in our project. We realize that we did't come back on some of the doubts requested by the designers. It will be inequitable to the designers who prerequisite our feedback. We also appreciate the comprehension of the community in this postponement.
Reason: Designers,
We really apreciate all the time and effort you put on our project. From the begining we ask for 3 pages, so now we will leave the 10 finalist and provide some extra time to submit the other 2 pages.
We will race the price in 10%
Target Market(s)
Our customers average investors works as employees and want to have a second income or business without spending time. (People from 35 to 50)
Industry/Entity Type
Finance
Requirements
Should not have
- FLASH

```html
<!DOCTYPE html>
<html lang="fr">
<head>
<meta charset="utf-8">
<title>BRAMLEY – Home</title>
<link href="https://fonts.googleapis.com/css2?family=Arimo:wght@400;700&family=Maven+Pro:wght@400;500&display=swap" rel="stylesheet">
<style>
:root{
  --olive:#6b681b;
  --band:#4e4946;
  --ink:#2b2b2b;
  --text:#3a3a3a;
  --page:#f4f4f4;
  --white:#ffffff;
  --rule:#dcdcdc;
  --btn:#3b3b3b;
}
*{box-sizing:border-box;margin:0;padding:0}
html,body{width:1083px;height:1200px;overflow:hidden}
body{background:var(--page);font-family:"Maven Pro",sans-serif;color:var(--text);position:relative}
.header-band{position:absolute;left:0;top:0;width:1083px;height:177px;background:var(--white);border-bottom:1px solid #e8e8e8}
.brand{position:absolute;left:123px;top:48px;display:flex;align-items:center;gap:8px;font-family:"Arimo",sans-serif;font-weight:700;font-size:30px;color:var(--ink);letter-spacing:1px}
.brand-mark{width:16px;height:16px;background:var(--olive)}
.social{position:absolute;left:880px;top:32px;display:flex;gap:4px}
.social span{width:21px;height:21px;background:var(--olive);display:block}
.nav{position:absolute;left:500px;top:88px;display:flex;font-family:"Arimo",sans-serif;font-size:13px;color:var(--ink)}
.nav a{color:inherit;text-decoration:none;padding:2px 7px 4px;margin-right:46px}
.nav a.active{color:var(--olive);border-bottom:1px solid var(--olive)}
.search{position:absolute;left:792px;top:88px;width:168px;height:20px;border:1px solid #d6d6d6;background:#fff;font-size:8px;font-style:italic;color:#aaa;padding:5px 8px}
.search svg{position:absolute;right:5px;top:3px}
.hero{position:absolute;left:123px;top:126px;width:837px;height:486px;border:1px solid #cfcfcf;background:linear-gradient(100deg,#c9c7c5 0%,#e6e3df 35%,#cdd3de 55%,#e9e6e2 70%,#7fae45 92%,#a9cc6e 100%)}
.dots{position:absolute;left:516px;top:632px;display:flex;gap:6px}
.dots i{width:8px;height:8px;border-radius:50%;background:#b5b5b5;display:block}
.dots i.on{background:var(--olive)}
.rule{position:absolute;left:123px;width:837px;height:1px;background:var(--rule)}
.feature{position:absolute;top:702px;width:185px}
.feature-head{display:flex;align-items:center;gap:8px;font-family:"Arimo",sans-serif;font-size:16px;color:var(--ink);white-space:nowrap}
.icon{width:41px;height:41px;border-radius:50%;background:var(--olive);display:flex;align-items:center;justify-content:center;color:#fff;font-size:27px;font-weight:700;flex:none}
.feature p{margin-top:28px;font-size:11px;line-height:16.3px;height:66px}
.btn{display:inline-block;background:var(--btn);color:#fff;font-size:11px;padding:2px 9px 3px;border-radius:2px}
.feature .btn{margin-top:12px}
.panel{position:absolute;top:932px;height:222px;background:#fff;border:1px solid #e0e0e0;border-radius:12px;overflow:hidden}
.panel h2{height:38px;background:var(--band);color:#fff;font-family:"Arimo",sans-serif;font-weight:400;font-size:19px;padding:9px 16px}
.welcome{left:123px;width:555px}
.welcome .body{padding:19px 40px 0 16px;font-size:10.6px;line-height:13.5px}
.welcome .body p{margin-bottom:13px}
.pill{display:inline-block;background:var(--btn);color:#fff;font-size:11px;padding:2px 8px 3px;border-radius:10px}
.testimonials{left:693px;width:267px}
.quote{display:flex;gap:12px;padding:0 8px 0 16px}
.quote:first-of-type{margin-top:18px}
.avatar{width:48px;height:45px;flex:none;background:linear-gradient(135deg,#d9c8b8,#8a6f5c);border:2px solid #eee}
.quote .date{color:var(--olive);font-size:10.5px}
.quote .msg{font-size:9.8px;line-height:13px;color:var(--ink)}
.quote .who{font-size:9.5px;font-weight:700;font-style:italic;margin-bottom:10px}
.testimonials .pill{margin:4px 0 0 16px}
.footer{position:absolute;left:123px;top:1173px;width:837px;font-size:9px;color:var(--ink);display:flex;justify-content:space-between}
.footer nav span{margin:0 5px}
</style>
</head>
<body>
<div class="header-band"></div>
<div class="brand"><span class="brand-mark"></span>BRAMLEY</div>
<div class="social" aria-label="Social links"><span></span><span></span><span></span></div>
<nav class="nav"><a class="active">Home</a><a>About Us</a><a>Properties</a></nav>
<div class="search">Enter your search here...
  <svg width="12" height="12" viewBox="0 0 12 12"><circle cx="5" cy="5" r="3.6" fill="none" stroke="#888" stroke-width="1.6"/><line x1="7.6" y1="7.6" x2="11" y2="11" stroke="#888" stroke-width="1.8"/></svg>
</div>

<div class="hero" role="img" aria-label="Photo of a smiling couple receiving house keys from an agent"></div>
<div class="dots"><i class="on"></i><i></i><i></i><i></i></div>
<div class="rule" style="top:660px"></div>

<section class="feature" style="left:123px">
  <div class="feature-head"><span class="icon">$</span>FOR INVESTORS</div>
  <p>Le Lorem Ipsum est simplement du faux texte employé dans la compo-sition et la mise en page avant impression.</p>
  <span class="btn">More</span>
</section>
<section class="feature" style="left:332px">
  <div class="feature-head"><span class="icon"><svg width="22" height="20" viewBox="0 0 22 20"><path d="M1 2h4l3 10h10l2-7H7" fill="none" stroke="#fff" stroke-width="2.4" stroke-linejoin="round"/><circle cx="9" cy="16.5" r="2" fill="#fff"/><circle cx="16" cy="16.5" r="2" fill="#fff"/></svg></span>FOR BUYERS</div>
  <p>An sait depuis longtemps que travailler avec du texte lisible et contenant du sens est source de distractions.</p>
  <span class="btn">More</span>
</section>
<section class="feature" style="left:541px">
  <div class="feature-head"><span class="icon"><svg width="20" height="22" viewBox="0 0 20 22"><rect x="2" y="2" width="16" height="12" fill="#fff"/><line x1="10" y1="14" x2="10" y2="21" stroke="#fff" stroke-width="1.5"/></svg></span>FOR SELLERS</div>
  <p>Plusieurs versions sont apparues avec le temps, parfois par accident, souvent intentionnellement histoire d'y rajouter de petits.</p>
  <span class="btn">More</span>
</section>
<section class="feature" style="left:751px">
  <div class="feature-head"><span class="icon"><svg width="24" height="20" viewBox="0 0 24 20"><path d="M12 1L1 11h3v8h6v-6h4v6h6v-8h3z" fill="#fff"/></svg></span>FOR HOMEOWNERS</div>
  <p>L'extrait standard de Lorem Ipsum utilisé depuis le XVIè siècle est reproduit ci-dessous pour les curieux.</p>
  <span class="btn">More</span>
</section>

<div class="rule" style="top:908px"></div>

<section class="panel welcome">
  <h2>WELCOME TO BRAMLEY</h2>
  <div class="body">
    <p>Le Lorem Ipsum est simplement du faux texte employé dans la composition et la mise en page avant impression. Le Lorem Ipsum est le faux texte standard de l'imprimerie depuis les années 1500.</p>
    <p>Quand un peintre anonyme assembla ensemble des morceaux de texte pour réaliser un livre spéci-men de polices de texte. Il n'a pas fait que survivre cinq siècles, mais s'est aussi adapté à la bureau-tique informatique, sans que son contenu n'en soit modifié. Il a été popularisé dans les années 1960.</p>
    <p>Grâce à la vente de feuilles Transfix contenant des passages du Lorem Ipsum, et, plus récemment, par son inclusion dans des applications de mise en page de texte, comme Folio Composer.</p>
    <span class="pill">More</span>
  </div>
</section>

<section class="panel testimonials">
  <h2>TESTIMONIALS</h2>
  <div class="quote">
    <div class="avatar" role="img" aria-label="Client portrait"></div>
    <div><div class="date">14-12-2012</div><div class="msg">On sait depuis longtemps que travail-ler avec du texte lisible etcon.</div><div class="who">Marcus Hale</div></div>
  </div>
  <div class="quote">
    <div class="avatar" role="img" aria-label="Client portrait"></div>
    <div><div class="date">14-12-2012</div><div class="msg">On sait depuis longtemps que travailler avec du texte lisible etcon.</div><div class="who">Marcus Hale</div></div>
  </div>
  <span class="pill">More</span>
</section>

<footer class="footer">
  <nav>Home<span>|</span>About Us<span>|</span>Properties</nav>
  <div>© Copyrights 2012 All rights Reserved</div>
</footer>
</body>
</html>
```